Velmor Stationery Design

We need Business Card, Letterhead, #10 Envelope , 3" x 4" Mailing Label, and email signature block. Also need "Aircraft Services" added small under the logo on everything except the email signature block. "Aircraft Services" should be in a simple font to to conflict with or distract from the logo. Our address info is:
4817 Halvend Loop NW
Brantwick, GA 30592
P 555.208.3146
C 555.208.3146 (for biz cards only)
glen@velmorjet.example (for biz cards only)
Website velmorjet.example
Feel free to play around with colors but I expect that black or gray will work best for the address/phone info etc.

Target Market(s)

Aircraft owners

Industry/Entity Type

Aviation

Colors

Designer to choose only greyscale colors for use in the design.

Requirements
Must have
• Clean and sophisticated design -

```html
<!DOCTYPE html>
<html lang="en">
<head>
<meta charset="utf-8">
<title>Velmor Email Signature</title>
<link rel="stylesheet" href="https://fonts.googleapis.com/css2?family=Montserrat:wght@400;500;600&display=swap">
<style>
  :root {
    --brand-blue: #0a74d4;
    --text-grey: #3d3d3d;
    --band-grey: #8c8c8c;
    --card-white: #ffffff;
    --page-bg: #e6e6e6;
  }
  * { margin: 0; padding: 0; box-sizing: border-box; }
  html, body {
    width: 1200px; height: 1200px; overflow: hidden;
    background: var(--page-bg);
    font-family: "Montserrat", Arial, sans-serif;
  }
  .signature {
    position: absolute; left: 39px; top: 463px;
    width: 1122px; height: 274px;
    background: var(--card-white);
  }
  .contact-block { position: absolute; left: 79px; top: 20px; }
  .full-name {
    color: var(--brand-blue); font-weight: 600;
    font-size: 44px; line-height: 1; letter-spacing: 0.2px;
  }
  .position {
    color: var(--text-grey); font-weight: 400;
    font-size: 26px; line-height: 1; margin-top: 6px;
  }
  .contact-list { list-style: none; margin-top: 14px; }
  .contact-item {
    display: flex; align-items: flex-start;
    color: var(--text-grey); font-size: 26px; line-height: 30px;
    margin-bottom: 6px;
  }
  .contact-icon { width: 28px; height: 30px; margin-right: 6px; flex: none; fill: var(--brand-blue); }
  .address { line-height: 26px; margin-top: 4px; }
  .brand-name {
    position: absolute; left: 630px; top: 96px;
    width: 420px; text-align: center;
    color: var(--brand-blue); font-weight: 600;
    font-size: 62px; letter-spacing: 4px; line-height: 1;
  }
  .footer-band { position: absolute; left: 0; bottom: 0; width: 1122px; height: 23px; display: block; }
  .band-blue { fill: var(--brand-blue); }
  .band-grey { fill: var(--band-grey); }
</style>
</head>
<body>
  <div class="signature">
    <div class="contact-block">
      <div class="full-name">FULL NAME</div>
      <div class="position">POSITION</div>
      <ul class="contact-list">
        <li class="contact-item">
          <svg class="contact-icon" viewBox="0 0 24 24" aria-hidden="true"><path d="M6.6 10.8a15.2 15.2 0 0 0 6.6 6.6l2.2-2.2a1 1 0 0 1 1-.25 11.4 11.4 0 0 0 3.6.57 1 1 0 0 1 1 1V20a1 1 0 0 1-1 1A17 17 0 0 1 3 4a1 1 0 0 1 1-1h3.5a1 1 0 0 1 1 1c0 1.25.2 2.45.57 3.6a1 1 0 0 1-.25 1z"/></svg>
          <span>P 555.208.3146</span>
        </li>
        <li class="contact-item">
          <svg class="contact-icon" viewBox="0 0 24 24" aria-hidden="true"><path d="M12 2a10 10 0 1 0 0 20 10 10 0 0 0 0-20zm6.9 6h-2.9a15.6 15.6 0 0 0-1.4-3.6A8 8 0 0 1 18.9 8zM12 4c.8 1.2 1.5 2.5 1.9 4h-3.8c.4-1.5 1.1-2.8 1.9-4zM4.3 14a8 8 0 0 1 0-4h3.4a16 16 0 0 0 0 4zm.8 2h2.9c.3 1.3.8 2.5 1.4 3.6A8 8 0 0 1 5.1 16zM8 8H5.1a8 8 0 0 1 4.3-3.6C8.8 5.5 8.3 6.7 8 8zm4 12c-.8-1.2-1.5-2.5-1.9-4h3.8c-.4 1.5-1.1 2.8-1.9 4zm2.3-6H9.7a14.6 14.6 0 0 1 0-4h4.6a14.6 14.6 0 0 1 0 4zm.3 5.6c.6-1.1 1.1-2.3 1.4-3.6h2.9a8 8 0 0 1-4.3 3.6zm1.7-5.6a16 16 0 0 0 0-4h3.4a8 8 0 0 1 0 4z"/></svg>
          <span>velmorjet.example</span>
        </li>
        <li class="contact-item">
          <svg class="contact-icon" viewBox="0 0 24 24" aria-hidden="true"><path d="M12 2a7 7 0 0 0-7 7c0 5.2 7 13 7 13s7-7.8 7-13a7 7 0 0 0-7-7zm0 10.5a3.5 3.5 0 1 1 0-7 3.5 3.5 0 0 1 0 7z"/></svg>
          <span class="address">4817 Halvend Loop NW<br>Brantwick, GA 30592</span>
        </li>
      </ul>
    </div>
    <div class="brand-name">VELMOR</div>
    <svg class="footer-band" viewBox="0 0 1122 23" aria-hidden="true">
      <polygon class="band-blue" points="0,0 552,0 539,23 0,23"/>
      <polygon class="band-grey" points="564,0 1122,0 1122,23 551,23"/>
    </svg>
  </div>
</body>
</html>
```